Business Advisory Firm Business Card

A clean, very upscale looking business card. Not crowded.

Please include logo (attached) and:

Daria K. Pellworth
Four Marlow Court
New York, NY 10023
tel: (917) 555-0143
fax: (646) 555-0172
email: dpellworth@quarrystoneconsultants.example
website: www.quarrystoneconsultants.example

Target Market(s)

Business clients. Often real estate development firms, other advisory firms or growing companies that need assistance. I would like a card that looks impressive and confident.

Industry/Entity Type

Business

Colors

Designer to choose colors to be used in the design.

Requirements
Must have
• Impressive and confident. Please include logo.
Should not have
• nothing flashy...

```html
<!DOCTYPE html>
<html lang="en">
<head>
<meta charset="utf-8">
<title>Quarrystone Advisory Services – Business Card</title>
<link href="https://fonts.googleapis.com/css2?family=Open+Sans:wght@400;600&family=Roboto+Condensed:wght@700&display=swap" rel="stylesheet">
<style>
  :root {
    --page-bg: #e6e6e3;
    --card-bg: #ffffff;
    --card-shade: #ececec;
    --ink: #3a3a3a;
    --ink-soft: #555555;
    --rule: #8a8a8a;
    --brand-green: #5a7f2c;
    --brand-green-light: #7fa33a;
    --band-grey: #b5b5b5;
  }
  * { margin: 0; padding: 0; box-sizing: border-box; }
  html, body {
    width: 1200px; height: 600px; overflow: hidden;
    background: var(--page-bg);
  }
  .card {
    position: absolute; left: 100px; top: 15px;
    width: 1000px; height: 570px;
    background: linear-gradient(135deg, var(--card-bg) 55%, var(--card-shade));
    box-shadow: 0 6px 18px rgba(0,0,0,0.18);
    overflow: hidden;
    font-family: "Open Sans", Arial, sans-serif;
    color: var(--ink);
  }
  .brand {
    position: absolute; left: 80px; top: 95px;
    display: flex; align-items: center; gap: 34px;
  }
  .brand-square {
    width: 120px; height: 120px;
    background: var(--brand-green-light);
  }
  .brand-name {
    font-weight: 600; font-size: 42px; line-height: 44px;
    letter-spacing: 1px; text-transform: uppercase;
    color: var(--ink);
  }
  .name-row {
    position: absolute; left: 240px; top: 272px; width: 700px;
    display: flex; align-items: center; gap: 18px;
  }
  .divider { height: 2px; background: var(--rule); }
  .divider-long { flex: 1; }
  .divider-short { width: 50px; flex: none; }
  .person-name {
    flex: none;
    font-family: "Roboto Condensed", "Arial Narrow", sans-serif;
    font-weight: 700; font-size: 40px; line-height: 50px;
    color: var(--brand-green); white-space: nowrap;
  }
  .contacts {
    position: absolute; left: 240px; top: 336px;
    list-style: none;
  }
  .contacts li {
    display: flex; align-items: center; gap: 16px;
    font-size: 23px; line-height: 34px; color: var(--ink-soft);
  }
  .contacts svg { width: 22px; height: 22px; flex: none; }
  .band {
    position: absolute; left: 0; bottom: 0; width: 1000px; height: 46px;
  }
</style>
</head>
<body>
  <main class="card">
    <div class="brand">
      <div class="brand-square"></div>
      <div class="brand-name">Quarrystone<br>Advisory<br>Services, Inc.</div>
    </div>

    <div class="name-row">
      <div class="divider divider-long"></div>
      <div class="person-name">Daria K. Pellworth</div>
      <div class="divider divider-short"></div>
    </div>

    <ul class="contacts">
      <li>
        <svg viewBox="0 0 24 24" aria-hidden="true"><path fill="#5a7f2c" d="M6.6 10.8a15 15 0 0 0 6.6 6.6l2.2-2.2c.3-.3.7-.4 1-.2 1.1.4 2.3.6 3.6.6.6 0 1 .4 1 1V20c0 .6-.4 1-1 1A17 17 0 0 1 3 4c0-.6.4-1 1-1h3.5c.6 0 1 .4 1 1 0 1.3.2 2.5.6 3.6.1.3 0 .7-.2 1z"/></svg>
        (917) 555-0143
      </li>
      <li>
        <svg viewBox="0 0 24 24" aria-hidden="true"><rect x="3" y="9" width="18" height="11" rx="2" fill="#5a7f2c"/><rect x="7" y="3" width="10" height="7" fill="#5a7f2c"/><rect x="7" y="13" width="10" height="2" fill="#fff"/></svg>
        (646) 555-0172
      </li>
      <li>
        <svg viewBox="0 0 24 24" aria-hidden="true"><rect x="2" y="5" width="20" height="14" rx="2" fill="#5a7f2c"/><path d="M3 6l9 7 9-7" stroke="#fff" stroke-width="2" fill="none"/></svg>
        dpellworth@quarrystoneconsultants.example
      </li>
      <li>
        <svg viewBox="0 0 24 24" aria-hidden="true"><circle cx="12" cy="12" r="10" fill="#5a7f2c"/><path d="M2 12h20M12 2c3 3 3 17 0 20M12 2c-3 3-3 17 0 20" stroke="#fff" stroke-width="1.5" fill="none"/></svg>
        www.quarrystoneconsultants.example
      </li>
      <li>
        <svg viewBox="0 0 24 24" aria-hidden="true"><path fill="#5a7f2c" d="M12 2a7 7 0 0 0-7 7c0 5 7 13 7 13s7-8 7-13a7 7 0 0 0-7-7zm0 9.5A2.5 2.5 0 1 1 12 6.5a2.5 2.5 0 0 1 0 5z"/></svg>
        Four Marlow Court, New York, NY 10023
      </li>
    </ul>

    <svg class="band" viewBox="0 0 1000 46" preserveAspectRatio="none" aria-hidden="true">
      <rect x="0" y="0" width="1000" height="46" fill="var(--brand-green)"/>
      <polygon points="900,0 1000,0 1000,46 870,46" fill="var(--band-grey)"/>
    </svg>
  </main>
</body>
</html>
```